Corvid Lens Studio Business Card Design

I need a business card designed for a photography business based in Perth, Western Australia called Corvid Lens Studio.

We specialise in wedding, event photography and portrait photography.

The business card must borrow the style of the attached logo.

The hex codes for the colours in the logo are:
#ED1D85 - Pink
#89C23E - Green
#37282F - Black

The name on the card will be:
Name: Tobiah
Phone: 0417395268
Website: www.corvidlensstudio.com.au
Facebook: corvidlensstudio

I am open and happy to accept creative concepts.

Industry/Entity Type

Business

```html
<!DOCTYPE html>
<html lang="en">
<head>
<meta charset="utf-8">
<title>Corvid Lens Studio – Business Card</title>
<link rel="stylesheet" href="https://fonts.googleapis.com/css2?family=Cinzel:wght@400;700&display=swap">
<style>
  :root {
    --pink: #ED1D85;
    --green: #89C23E;
    --ink: #37282F;
    --ink-soft: #4a4a4a;
    --card: #fbfbfb;
    --backdrop: #e3e3e3;
  }
  * { margin: 0; padding: 0; box-sizing: border-box; }
  html, body {
    width: 1200px;
    height: 720px;
    overflow: hidden;
    background: var(--backdrop);
  }
  .canvas {
    position: relative;
    width: 1200px;
    height: 720px;
  }
  .card {
    position: absolute;
    top: 242px;
    width: 420px;
    height: 239px;
    background: var(--card);
    font-family: "Cinzel", serif;
    color: var(--ink);
    text-align: center;
  }
  .card--back { left: 147px; }
  .card--front { left: 633px; }

  .person {
    position: absolute;
    top: 87px;
    left: 0;
    right: 0;
    line-height: 1.1;
  }
  .person__name {
    color: var(--pink);
    font-weight: 700;
    font-size: 13px;
    letter-spacing: 0.02em;
  }
  .person__role {
    font-size: 9.5px;
    color: var(--ink);
  }

  .contact {
    position: absolute;
    top: 166px;
    left: 0;
    right: 0;
    list-style: none;
    font-size: 9.5px;
    line-height: 12px;
  }
  .contact__label {
    color: var(--pink);
    font-weight: 700;
    margin-right: 4px;
  }
  .contact__value { color: var(--ink); }

  .brand-dot {
    position: absolute;
    top: 68px;
    left: 176px;
    width: 68px;
    height: 68px;
  }
  .brand-name {
    position: absolute;
    top: 169px;
    left: 0;
    right: 0;
    font-size: 12.5px;
    font-weight: 400;
    letter-spacing: 0.78em;
    padding-left: 0.78em;
    color: var(--ink-soft);
    white-space: nowrap;
  }
</style>
</head>
<body>
<main class="canvas">
  <section class="card card--back" aria-label="Card back with contact details">
    <div class="person">
      <p class="person__name">Tobiah</p>
      <p class="person__role">Photographer</p>
    </div>
    <ul class="contact">
      <li><span class="contact__label">Phone :</span><span class="contact__value">0417395268</span></li>
      <li><span class="contact__label">Facebook :</span><span class="contact__value">corvidlensstudio</span></li>
      <li><span class="contact__label">Web :</span><span class="contact__value">www.corvidlensstudio.com.au</span></li>
    </ul>
  </section>

  <section class="card card--front" aria-label="Card front with studio name">
    <svg class="brand-dot" viewBox="0 0 68 68" aria-hidden="true">
      <circle cx="34" cy="34" r="33" fill="var(--pink)"/>
    </svg>
    <p class="brand-name">CORVID LENS STUDIO</p>
  </section>
</main>
</body>
</html>
```